Home Baker of fresh bakes, muffins, cookies & treats.

I am looking for business cards for my home baking business called " Mmm Bex-O Plenty " - I want them to be super cute and girly, yet simple and modern at the same time. Pastel colours is what I envision with the main colour being baby pink.

```html
<!DOCTYPE html>
<html lang="en">
<head>
<meta charset="utf-8">
<title>Mmm Bex-O Plenty business cards</title>
<link rel="stylesheet" href="https://fonts.googleapis.com/css2?family=Delius&family=Didact+Gothic&family=Yellowtail&display=swap">
<style>
  :root {
    --page: #e9e6e6;
    --baby-pink: #f19c9b;
    --lace: #f9d6d5;
    --pattern-light: #fce6e5;
    --pattern-mid: #f7c6c5;
    --white: #ffffff;
  }
  * { margin: 0; padding: 0; box-sizing: border-box; }
  html, body { width: 1200px; height: 903px; overflow: hidden; }
  body { background: var(--page); position: relative; }

  .card {
    position: absolute;
    width: 540px;
    height: 310px;
    border-radius: 16px;
    overflow: hidden;
    box-shadow: 0 6px 18px rgba(0,0,0,.18);
  }

  /* Contact card */
  .card--contact { left: 70px; top: 110px; background: var(--baby-pink); }
  .top-strip {
    position: absolute; left: 0; right: 0; top: 0; height: 20px; background: var(--white);
  }
  .lace-band {
    position: absolute; left: 0; right: 0; height: 28px;
  }
  .lace-band--top {
    top: 20px;
    background: linear-gradient(180deg, var(--white), var(--lace) 55%, var(--baby-pink));
  }
  .lace-band--bottom {
    bottom: 0;
    background: linear-gradient(0deg, var(--white), var(--lace) 55%, var(--baby-pink));
  }

  .contact-body {
    position: absolute; left: 0; right: 0; top: 72px;
    text-align: center; color: var(--white);
  }
  .brand-name {
    font-family: "Delius", sans-serif;
    font-weight: 400;
    line-height: 1.1;
    letter-spacing: .5px;
  }
  .card--contact .brand-name { font-size: 36px; }
  .tagline {
    font-family: "Didact Gothic", sans-serif;
    letter-spacing: .6px;
  }
  .card--contact .tagline { font-size: 15px; margin-top: 6px; }
  .person-name {
    font-family: "Yellowtail", cursive;
    font-size: 32px;
    margin-top: 10px;
    line-height: 1.1;
  }
  .contact-line {
    font-family: "Didact Gothic", sans-serif;
    font-size: 13px;
    letter-spacing: .6px;
    margin-top: 5px;
  }

  /* Brand card */
  .card--brand { left: 590px; top: 475px; background: var(--white); }
  .treat-pattern {
    position: absolute; inset: 0;
    background: linear-gradient(135deg, var(--pattern-light), var(--pattern-mid) 50%, var(--pattern-light));
  }
  .brand-band {
    position: absolute; left: 0; right: 0; top: 98px; height: 118px;
    background: var(--baby-pink);
    display: flex; flex-direction: column; align-items: center; justify-content: center;
    color: var(--white); text-align: center;
  }
  .card--brand .brand-name { font-size: 46px; }
  .card--brand .tagline { font-size: 18px; margin-top: 6px; }
</style>
</head>
<body>

  <section class="card card--contact" aria-label="Contact side of the business card">
    <div class="top-strip"></div>
    <div class="lace-band lace-band--top" role="img" aria-label="White lace trim border"></div>
    <div class="contact-body">
      <h1 class="brand-name">Mmm Bex-O Plenty</h1>
      <p class="tagline">fresh bakes, muffins, cookies &amp; treats.</p>
      <p class="person-name">Clara Moss</p>
      <p class="contact-line">084-5512-0937</p>
      <p class="contact-line">info@mmmbexoplenty.com</p>
    </div>
    <div class="lace-band lace-band--bottom" role="img" aria-label="White lace trim border"></div>
  </section>

  <section class="card card--brand" aria-label="Brand side of the business card">
    <div class="treat-pattern" role="img" aria-label="Pattern of pink baked treat icons on white"></div>
    <div class="brand-band">
      <h2 class="brand-name">Mmm Bex-O Plenty</h2>
      <p class="tagline">fresh bakes, muffins, cookies &amp; treats.</p>
    </div>
  </section>

</body>
</html>
```